EventVora Business Card

EventVora is a full-service meeting planning and management company specializing in turnkey corporate meetings and event planning. We focus on all the little details that make your event great so you don't have to worry about a thing. if you can visualize it, we can do it.

We are a small business - all women. We want our business cards to reflect our creative nature with a little touch of our spunky personality. We want to WOW from the start with these business cards.

website: www.eventvora-example.com

Contact Information for Business Card

I would like printing on front and back. back side should include our motto, "Always do what's expected, plus a little bit more!" and website with a design like attached. I would like the background color to be a blue that matches our logo. The front will probably need to be white and will need to include our logo and name, title and contact info. any additional design/color added would be nice as long as it flows with the design on the back of the card. I have attached two examples of other company's cards (dog walking & squish) as an example for the front.

```html
<!DOCTYPE html>
<html lang="en">
<head>
<meta charset="utf-8">
<title>EventVora Business Card</title>
<link href="https://fonts.googleapis.com/css2?family=Quicksand:wght@500;700&family=Dancing+Script:wght@500&family=Montserrat:wght@400&display=swap" rel="stylesheet">
<style>
  :root {
    --stage: #bdbdbd;
    --card: #ffffff;
    --blue: #0a74bb;
    --blue-deep: #0866a8;
    --orange: #f07a12;
    --ink: #1c1c1c;
    --gold: #ecc32e;
  }
  * { box-sizing: border-box; margin: 0; padding: 0; }
  html, body { width: 1200px; height: 837px; overflow: hidden; }
  body {
    background: var(--stage);
    font-family: "Quicksand", sans-serif;
    color: var(--ink);
    position: relative;
  }
  .card {
    position: absolute;
    width: 525px;
    height: 300px;
    background: var(--card);
    box-shadow: 0 6px 18px rgba(0,0,0,0.18);
    overflow: hidden;
    top: 268px;
  }
  .card--back { left: 45px; }
  .card--front { left: 630px; }

  /* back */
  .back-band {
    position: absolute; left: 0; right: 0; bottom: 0; height: 34px;
    display: flex;
  }
  .back-band__orange { width: 46%; background: var(--orange); }
  .back-band__blue { flex: 1; background: var(--blue); }
  .flourish {
    position: absolute; left: 50%; transform: translateX(-50%);
    width: 80px; height: 30px; border-radius: 15px;
    background: linear-gradient(90deg, rgba(236,195,46,0.35), rgba(236,195,46,0.8), rgba(236,195,46,0.35));
  }
  .flourish--top { top: 62px; }
  .flourish--bottom { top: 150px; }
  .motto {
    position: absolute; top: 102px; left: 0; right: 0;
    text-align: center;
    font-family: "Dancing Script", cursive;
    font-size: 27px; font-weight: 500;
  }
  .back-web {
    position: absolute; top: 200px; left: 0; right: 0;
    text-align: center;
    font-family: "Montserrat", sans-serif;
    font-size: 10px; letter-spacing: 5px; text-transform: uppercase;
  }

  /* front */
  .brand {
    position: absolute; left: 34px; top: 48px;
    display: flex; align-items: center; gap: 10px;
  }
  .brand__dot { width: 54px; height: 54px; border-radius: 50%; background: var(--blue); }
  .brand__name { font-size: 36px; font-weight: 500; color: var(--blue); letter-spacing: -0.5px; }
  .brand__tagline {
    position: absolute; left: 98px; top: 104px;
    font-size: 11px; font-style: italic; color: var(--ink);
  }
  .divider {
    position: absolute; left: 292px; top: 40px; width: 1px; height: 128px;
    background: var(--blue);
  }
  .contact { position: absolute; left: 308px; top: 44px; font-size: 13px; line-height: 1.4; }
  .contact__name { color: var(--blue); font-weight: 700; font-size: 15px; letter-spacing: 0.5px; }
  .contact__title { font-size: 12px; margin-bottom: 4px; }
  .contact__row { display: flex; align-items: center; gap: 6px; }
  .contact__icon {
    width: 14px; height: 14px; border-radius: 3px; background: var(--blue);
    display: inline-flex; align-items: center; justify-content: center; flex: none;
  }
  .front-swoosh { position: absolute; left: 0; bottom: 0; width: 525px; height: 130px; }
</style>
</head>
<body>

<section class="card card--back" aria-label="Card back">
  <div class="flourish flourish--top" role="img" aria-label="Gold swirl ornament"></div>
  <p class="motto">Always do what's expected, plus a little bit more!</p>
  <div class="flourish flourish--bottom" role="img" aria-label="Gold swirl ornament"></div>
  <p class="back-web">www.eventvora-example.com</p>
  <div class="back-band">
    <div class="back-band__orange"></div>
    <div class="back-band__blue"></div>
  </div>
</section>

<section class="card card--front" aria-label="Card front">
  <div class="brand">
    <span class="brand__dot"></span>
    <span class="brand__name">EventVora</span>
  </div>
  <p class="brand__tagline">meeting planning &amp; management</p>
  <div class="divider"></div>
  <div class="contact">
    <p class="contact__name">DANA MERCER</p>
    <p class="contact__title">Manager</p>
    <p>4820 Lakeview Rd. 12</p>
    <p>Brookfield, TX 75000</p>
    <p class="contact__row">
      <span class="contact__icon"><svg width="9" height="9" viewBox="0 0 10 10"><path d="M2 1 L4 1 L4.6 3 L3.5 3.8 Q4.5 5.8 6.2 6.5 L7 5.4 L9 6 L9 8 Q5 9 2.5 6 Q1 4 2 1Z" fill="#fff"/></svg></span>555-014-2290
    </p>
    <p class="contact__row">
      <span class="contact__icon"><svg width="9" height="9" viewBox="0 0 10 10"><rect x="1" y="2.5" width="8" height="5.5" fill="none" stroke="#fff" stroke-width="1"/><path d="M1 2.5 L5 6 L9 2.5" fill="none" stroke="#fff" stroke-width="1"/></svg></span>hello@eventvora-example.com
    </p>
    <p class="contact__row">
      <span class="contact__icon"><svg width="9" height="9" viewBox="0 0 10 10"><circle cx="5" cy="5" r="3.8" fill="none" stroke="#fff" stroke-width="1"/><path d="M1.2 5 H8.8 M5 1.2 V8.8" stroke="#fff" stroke-width="0.8"/></svg></span>www.eventvora-example.com
    </p>
  </div>
  <svg class="front-swoosh" viewBox="0 0 525 130" preserveAspectRatio="none" aria-hidden="true">
    <path d="M0 0 Q260 20 525 130 L525 130 L0 130 Z" fill="var(--orange)"/>
    <path d="M0 0 Q250 10 480 130 L0 130 Z" fill="#ffffff"/>
    <path d="M0 4 Q240 22 460 130 L0 130 Z" fill="var(--blue)"/>
    <path d="M0 22 Q220 50 400 130 L0 130 Z" fill="var(--blue-deep)" opacity="0.35"/>
  </svg>
</section>

</body>
</html>
```